Hip-Hop Artist Rex Tamber new album cover design for "Hollow Meridian"

Artist: Rex Tamber
Album Title: Hollow Meridian
I am attaching a un-edited picture to use & some sample images with the "Hollow Meridian" concept directions. I am hoping that the graphic designers accepting this challenge can do a better or different job than the 3 sample design images attached. I do like each of the 3 attached drafts(Draft, Draft2, Draft3) concepts. But, would like to see other creative design approaches and other possible affect. artwork ideas.
I am also attaching a number of random design that I also like the direction on.
Please let em know if you have any questions, and I will respond as quickly as possible.

```html
<!DOCTYPE html>
<html lang="en">
<head>
<meta charset="utf-8">
<title>Rex Tamber – Hollow Meridian</title>
<link href="https://fonts.googleapis.com/css2?family=Montserrat:wght@400&family=Permanent+Marker&family=Caveat+Brush&display=swap" rel="stylesheet">
<style>
  :root {
    --backdrop: #cfd0cc;
    --night-violet: #221a31;
    --plum: #3a1d3b;
    --deep-plum: #2a1a2e;
    --ash: #6f706a;
    --paper-grey: #a3a49c;
    --paper-light: #bdbeb6;
    --crimson: #d81f4f;
    --white: #ffffff;
  }
  html, body {
    margin: 0;
    padding: 0;
    width: 1200px;
    height: 850px;
    overflow: hidden;
    background: var(--backdrop);
  }
  .canvas {
    position: relative;
    width: 1200px;
    height: 850px;
  }
  .album-cover {
    position: absolute;
    left: 210px;
    top: 35px;
    width: 780px;
    height: 780px;
    overflow: hidden;
    box-shadow: 0 6px 18px rgba(0,0,0,0.18);
  }
  .cover-photo {
    position: absolute;
    inset: 0;
    background:
      radial-gradient(ellipse 90px 120px at 50% 14%, rgba(58,29,59,0.9) 0%, rgba(58,29,59,0) 100%),
      radial-gradient(ellipse 190px 420px at 50% 62%, rgba(34,22,40,0.95) 0%, rgba(34,22,40,0.85) 55%, rgba(34,22,40,0) 100%),
      radial-gradient(ellipse 200px 160px at 82% 42%, rgba(163,164,156,0.55) 0%, rgba(163,164,156,0) 100%),
      radial-gradient(ellipse 260px 150px at 20% 40%, rgba(163,164,156,0.45) 0%, rgba(163,164,156,0) 100%),
      radial-gradient(ellipse 320px 330px at 12% 85%, var(--paper-light) 0%, rgba(163,164,156,0.7) 45%, rgba(111,112,106,0) 100%),
      radial-gradient(ellipse 300px 220px at 85% 90%, rgba(163,164,156,0.75) 0%, rgba(111,112,106,0) 100%),
      linear-gradient(180deg, var(--night-violet) 0%, var(--plum) 38%, var(--ash) 75%, var(--paper-grey) 100%);
  }
  .cover-photo::after {
    content: "";
    position: absolute;
    inset: 0;
    background: linear-gradient(165deg, rgba(34,26,49,0.55) 0%, rgba(58,29,59,0.35) 40%, rgba(58,29,59,0) 70%);
  }
  .title-block {
    position: absolute;
    left: 0;
    right: 0;
    top: 300px;
    text-align: center;
    color: var(--white);
  }
  .artist-name {
    font-family: "Montserrat", sans-serif;
    font-weight: 400;
    font-size: 33px;
    letter-spacing: 1px;
    text-transform: uppercase;
    margin: 0;
    line-height: 1;
  }
  .album-title {
    margin: 0;
    font-weight: 400;
  }
  .album-title-main {
    display: block;
    font-family: "Permanent Marker", "Caveat Brush", cursive;
    font-weight: 400;
    font-size: 118px;
    line-height: 1;
    margin-top: 4px;
    text-transform: uppercase;
    letter-spacing: -3px;
    color: #f2f2f0;
    transform: rotate(-4deg);
  }
  .album-title-sub {
    position: relative;
    display: inline-block;
    margin-top: -14px;
    padding: 12px 22px 10px;
    background: var(--crimson);
    font-family: "Montserrat", sans-serif;
    font-weight: 400;
    font-size: 33px;
    letter-spacing: 1px;
    text-transform: uppercase;
    line-height: 1;
  }
</style>
</head>
<body>
  <main class="canvas">
    <section class="album-cover">
      <div class="cover-photo" role="img" aria-label="Moody photograph of the artist crouching on a floor scattered with paper sheets, tinted in dark violet"></div>
      <div class="title-block">
        <p class="artist-name">Rex Tamber</p>
        <h1 class="album-title">
          <span class="album-title-main">Hollow</span>
          <span class="album-title-sub">Meridian</span>
        </h1>
      </div>
    </section>
  </main>
</body>
</html>
```